New Company Business Card design

Looking for a corporate looking business card utilising my new logo design - the logo i would like embossed as one option and flat as another - simplistic but stylish - less is more - we are an import export business launching into the market - i would like a couple of options as main background - Grey or Black

```html
<!DOCTYPE html>
<html lang="en">
<head>
<meta charset="utf-8">
<title>Meridian Trade Partners – Business Card</title>
<link rel="stylesheet" href="https://fonts.googleapis.com/css2?family=Open+Sans:wght@400;600;700&display=swap">
<style>
  :root {
    --backdrop: #e6e7e9;
    --card-black: #080709;
    --card-white: #ffffff;
    --brand-blue: #2175be;
    --facet-blue: #6b8cc4;
    --text-light: #ffffff;
  }
  * { box-sizing: border-box; margin: 0; padding: 0; }
  html, body {
    width: 1200px;
    height: 1200px;
    overflow: hidden;
    background: var(--backdrop);
    font-family: "Open Sans", Arial, sans-serif;
  }
  .canvas { position: relative; width: 1200px; height: 1200px; }
  .card {
    position: absolute;
    left: 175px;
    width: 850px;
    height: 486px;
    overflow: hidden;
  }
  .card--front { top: 105px; background: var(--card-black); }
  .card--back { top: 631px; background: var(--card-white); }
  .card__art { position: absolute; inset: 0; width: 850px; height: 486px; }

  .brand {
    position: absolute;
    left: 0; right: 0;
    top: 350px;
    display: flex;
    justify-content: center;
    align-items: center;
    gap: 10px;
    color: var(--brand-blue);
    font-weight: 600;
    font-size: 19px;
    letter-spacing: 1.5px;
    text-transform: uppercase;
  }
  .brand__dot {
    width: 12px; height: 12px;
    border-radius: 50%;
    background: var(--brand-blue);
  }
  .front__rule {
    position: absolute;
    left: 405px; top: 404px;
    width: 40px; height: 3px;
    background: var(--brand-blue);
  }
  .front__web {
    position: absolute;
    left: 0; right: 0; top: 421px;
    text-align: center;
    color: var(--text-light);
    font-size: 12.5px;
    letter-spacing: 3px;
  }
  .front__web strong { font-weight: 700; }

  .holder {
    position: absolute;
    left: 81px; top: 263px;
    color: var(--brand-blue);
    line-height: 1;
  }
  .holder__name { font-size: 23px; font-weight: 400; letter-spacing: 0.3px; }
  .holder__name b { font-weight: 700; }
  .holder__title { margin-top: 4px; font-size: 16px; padding-left: 2px; }

  .contacts {
    position: absolute;
    left: 493px; top: 172px;
    list-style: none;
    color: var(--text-light);
    font-size: 13px;
  }
  .contacts__item {
    display: flex;
    align-items: center;
    gap: 22px;
    height: 29px;
    margin-bottom: 17px;
  }
  .contacts__icon {
    flex: none;
    width: 29px; height: 29px;
    border-radius: 50%;
    background: var(--text-light);
    display: flex; align-items: center; justify-content: center;
  }
  .contacts__text { line-height: 15px; letter-spacing: 0.2px; }
</style>
</head>
<body>
<main class="canvas">

  <section class="card card--front" aria-label="Card front">
    <svg class="card__art" viewBox="0 0 850 486">
      <polygon points="0,333 105,486 0,486" fill="var(--facet-blue)" role="img" aria-label="Blue faceted geometric corner decoration"/>
    </svg>
    <div class="brand"><span class="brand__dot"></span><span class="brand__name">Meridian Trade Partners</span></div>
    <div class="front__rule"></div>
    <p class="front__web">www.<strong>yourwebsite</strong>.com</p>
  </section>

  <section class="card card--back" aria-label="Card back">
    <svg class="card__art" viewBox="0 0 850 486">
      <polygon class="back__panel" points="433.6,0 850,0 850,486 192.8,486" fill="var(--card-black)"/>
      <polygon class="back__stripe" points="332.8,167.2 350.8,167.2 276.4,317.6 256.8,317.6" fill="var(--brand-blue)"/>
      <circle class="back__portrait" cx="138.4" cy="211.2" r="44.8" fill="var(--brand-blue)"/>
    </svg>

    <div class="holder">
      <p class="holder__name"><b>YOUR</b> NAME</p>
      <p class="holder__title">Solution Manager</p>
    </div>

    <ul class="contacts">
      <li class="contacts__item">
        <span class="contacts__icon">
          <svg width="13" height="13" viewBox="0 0 24 24" aria-hidden="true"><path d="M6.6 10.8a15.1 15.1 0 0 0 6.6 6.6l2.2-2.2c.3-.3.7-.4 1-.2 1.1.4 2.3.6 3.6.6.6 0 1 .4 1 1V20c0 .6-.4 1-1 1A17 17 0 0 1 3 4c0-.6.4-1 1-1h3.5c.6 0 1 .4 1 1 0 1.3.2 2.5.6 3.6.1.3 0 .7-.2 1l-2.3 2.2z" fill="var(--card-black)"/></svg>
        </span>
        <span class="contacts__text">012.345.6780<br>012.345.6780</span>
      </li>
      <li class="contacts__item">
        <span class="contacts__icon">
          <svg width="14" height="14" viewBox="0 0 24 24" aria-hidden="true" fill="none" stroke="var(--card-black)" stroke-width="1.8"><circle cx="12" cy="12" r="9"/><ellipse cx="12" cy="12" rx="4" ry="9"/><line x1="3" y1="12" x2="21" y2="12"/><line x1="4.5" y1="7.5" x2="19.5" y2="7.5"/><line x1="4.5" y1="16.5" x2="19.5" y2="16.5"/></svg>
        </span>
        <span class="contacts__text">info@website.com<br>www.website.com</span>
      </li>
      <li class="contacts__item">
        <span class="contacts__icon">
          <svg width="12" height="14" viewBox="0 0 24 28" aria-hidden="true"><path d="M12 1a9 9 0 0 0-9 9c0 6.8 9 17 9 17s9-10.2 9-17a9 9 0 0 0-9-9zm0 12.5a3.5 3.5 0 1 1 0-7 3.5 3.5 0 0 1 0 7z" fill="var(--card-black)"/></svg>
        </span>
        <span class="contacts__text">street name,place name</span>
      </li>
    </ul>
  </section>

</main>
</body>
</html>
```